Quolvex custom business card design

Need a authentic, innovative business card design for a new mobile app business. I am uploading a few screen images from our app for you to view. I would like app design theme to match business card design. I can also send logo images.

```html
<!DOCTYPE html>
<html lang="en">
<head>
<meta charset="utf-8">
<title>Quolvex business card</title>
<link rel="stylesheet" href="https://fonts.googleapis.com/css2?family=Montserrat:wght@500;700;800&display=swap">
<style>
  :root {
    --brand-purple: #622a8a;
    --brand-ink: #1e1e1e;
    --card-white: #ffffff;
    --text-ink: #222222;
    --backdrop: #e9e7e4;
  }
  * { box-sizing: border-box; margin: 0; padding: 0; }
  html, body {
    width: 900px; height: 1200px; overflow: hidden;
    background: var(--backdrop);
    font-family: "Montserrat", Arial, sans-serif;
    color: var(--text-ink);
  }
  .stage { position: relative; width: 900px; height: 1200px; }
  .card {
    position: absolute; left: 87px; width: 735px; height: 428px;
    background: var(--card-white); border-radius: 22px; overflow: hidden;
    box-shadow: 0 6px 14px rgba(0,0,0,0.18);
  }
  .card-front { top: 137px; }
  .card-back { top: 635px; }

  .person-name {
    position: absolute; left: 42px; top: 62px;
    font-size: 26px; font-weight: 700; color: var(--brand-purple);
  }
  .person-role {
    position: absolute; left: 40px; top: 96px;
    font-size: 18px; font-weight: 500;
  }
  .divider {
    position: absolute; left: 42px; width: 20px; height: 3px;
    background: var(--brand-purple);
  }
  .divider-top { top: 146px; }
  .divider-bottom { top: 252px; }
  .address {
    position: absolute; left: 40px; top: 178px;
    font-size: 18.5px; font-weight: 500; line-height: 25px;
  }
  .contact-list {
    position: absolute; left: 40px; top: 287px; list-style: none;
  }
  .contact-list li {
    display: flex; align-items: center; height: 30px;
    font-size: 18.5px; font-weight: 500;
  }
  .contact-list svg { width: 22px; height: 18px; margin-right: 14px; fill: var(--brand-purple); }

  .brand-dot {
    position: absolute; left: 440px; top: 52px;
    width: 254px; height: 254px; border-radius: 50%;
    background: var(--brand-purple);
  }
  .brand-name {
    position: absolute; font-weight: 800; color: var(--brand-ink);
    letter-spacing: -0.5px; line-height: 1;
  }
  .card-front .brand-name { left: 417px; top: 323px; font-size: 60px; }

  .back-disc {
    position: absolute; left: 30px; top: -240px;
    width: 560px; height: 560px; border-radius: 50%;
    background: var(--brand-purple);
  }
  .card-back .brand-name { left: 40px; top: 345px; font-size: 64px; }
</style>
</head>
<body>
<main class="stage">
  <section class="card card-front" aria-label="Business card front">
    <h1 class="person-name">Marlen Vask</h1>
    <p class="person-role">Manager</p>
    <span class="divider divider-top"></span>
    <p class="address">1187 Alder Crest Lane, Brenton<br>OR, Oregon, 97402</p>
    <span class="divider divider-bottom"></span>
    <ul class="contact-list">
      <li>
        <svg viewBox="0 0 24 20" aria-hidden="true"><path d="M3 6c0-2 3-4 9-4s9 2 9 4v2h-5V6H8v2H3zM7 9h10l3 9H4z"/><circle cx="12" cy="13.5" r="2.4" fill="#fff"/></svg>
        014 276 3958
      </li>
      <li>
        <svg viewBox="0 0 24 20" aria-hidden="true"><path d="M3 4h18v2l-9 6-9-6z"/><path d="M3 8l9 6 9-6v9H3z"/></svg>
        hello@Quolvex.com
      </li>
      <li>
        <svg viewBox="0 0 24 24" aria-hidden="true"><path fill="none" stroke="#622a8a" stroke-width="2" d="M12 2a10 10 0 1 0 0 20a10 10 0 1 0 0-20zM2 12h20M12 2c-3 3-4 6-4 10s1 7 4 10M12 2c3 3 4 6 4 10s-1 7-4 10"/></svg>
        www.Quolvex.com
      </li>
    </ul>
    <span class="brand-dot" aria-hidden="true"></span>
    <p class="brand-name">Quolvex</p>
  </section>

  <section class="card card-back" aria-label="Business card back">
    <span class="back-disc" aria-hidden="true"></span>
    <p class="brand-name">Quolvex</p>
  </section>
</main>
</body>
</html>
```